Quenford Pier Hall Museum Website (Design Only)

The Quenford Pier Hall is a newly renovated historical building in lower Manhattan. We are building a website for them so that tours and events can be scheduled. We have provided typography requirements along with many photographs. You are free to be creative with the use of the photographs in your design. There is no specific brand or color guidelines but the client did specify that they wanted the website to be clean, simple and elegant BUT to also reflect the vintage colors and feeling of the building. Please do NOT design the logo as we have a separate contest for the logo. We have provided a mock up of all website pages that we would like designed. however we encourage you to design and submit the home page an a few other pages first so we can provide feedback. The designs that you provide must be compatible with Wix.

```html
<!DOCTYPE html>
<html lang="en">
<head>
<meta charset="utf-8">
<title>Quenford Pier Hall Museum — Website Pages</title>
<link rel="stylesheet" href="https://fonts.googleapis.com/css2?family=Jost:wght@400;500&family=Barlow+Condensed:wght@300;400&display=swap">
<style>
:root{
  --stage:#111111;
  --page:#ffffff;
  --cream:#f2f1e9;
  --ink:#2b2b2b;
  --rule:#8a8a8a;
  --footer:#4b4b4b;
  --footer-ink:#e9e9e9;
  --accent:#f5a300;
  --sky-top:#2f7fd0;
  --sky-bottom:#cfe2f3;
  --gold:#a68a3a;
  --stone:#8c8b84;
  --mono-dark:#2a2a2a;
  --mono-light:#b9b9b9;
}
*{box-sizing:border-box;margin:0;padding:0}
html,body{width:1200px;height:4090px;overflow:hidden;background:var(--stage)}
body{position:relative;font-family:"Jost",sans-serif;color:var(--ink)}
.page{position:absolute;left:184px;width:830px;background:var(--page);overflow:hidden}
.page--home{top:84px;height:1646px}
.page--mission{top:1857px;height:617px}
.page--gallery{top:2514px;height:751px}
.page--history{top:3304px;height:616px}

/* header */
.site-header{position:absolute;top:0;left:0;right:0;height:60px;background:var(--page);z-index:2}
.brand{position:absolute;left:49px;top:0;width:106px;height:103px;background:var(--page);display:flex;flex-direction:column;align-items:center;justify-content:center;gap:8px;z-index:3}
.brand__mark{width:34px;height:34px;background:var(--ink)}
.brand__name{font-size:9px;font-weight:500;text-align:center;line-height:1.25}
.main-nav{position:absolute;right:70px;top:23px;display:flex;gap:22px;font-size:10px;font-weight:500}
.main-nav span.has-menu::after{content:" ⌄";font-size:9px}

/* footer */
.site-footer{position:absolute;left:0;right:0;bottom:0;height:56px;background:var(--footer);color:var(--footer-ink);display:flex;align-items:center;padding:0 0 0 91px;font-size:10px}
.site-footer nav{display:flex;gap:16px}
.social{position:absolute;right:58px;display:flex;gap:9px}
.social i{display:block;width:10px;height:10px;border-radius:50%;background:var(--footer-ink)}

.photo{display:block}

/* home */
.hero{position:absolute;top:60px;left:0;width:830px;height:329px;background:linear-gradient(180deg,var(--sky-top) 0%,var(--sky-bottom) 45%,var(--gold) 62%,#5a4a22 100%)}
.welcome{position:absolute;top:389px;left:0;width:830px;height:233px;background:var(--cream)}
.welcome h1{position:absolute;left:90px;top:45px;font-size:38px;font-weight:500;line-height:44px}
.welcome p{position:absolute;left:499px;top:55px;width:230px;font-family:"Barlow Condensed",sans-serif;font-weight:300;font-size:17px;line-height:22px}

.feature{position:absolute;top:668px;width:280px}
.feature--hours{left:100px}
.feature--history{left:425px}
.feature h2{font-size:19px;font-weight:400;padding-bottom:4px;border-bottom:1px solid var(--rule)}
.feature .photo{margin-top:16px;width:278px;height:163px}
.feature p{margin-top:14px;font-size:10px}
.btn{display:inline-flex;align-items:center;gap:6px;margin-top:12px;padding:5px 11px;background:var(--accent);border-radius:14px;font-size:10px;font-weight:500;color:var(--ink)}
.btn svg{width:14px;height:8px}

.events-title{position:absolute;left:95px;top:1014px;width:646px;height:73px;border-top:1px solid var(--rule);border-bottom:1px solid var(--rule);display:flex;align-items:center;justify-content:center;font-size:20px;margin-right:0}
.event{position:absolute;left:95px;width:646px;height:122px;display:flex;align-items:center;border-bottom:1px solid var(--rule)}
.event .photo{width:113px;height:113px;margin-left:3px}
.event__day{margin-left:23px;font-size:22px;width:36px}
.event__meta{font-size:11px;line-height:16px;margin-left:2px;width:66px}
.event__title{font-size:17px;font-weight:500;flex:1}
.event .btn{margin:0 16px 0 0;padding:4px 0;width:108px;justify-content:center;font-size:9px}

/* split pages */
.split__intro{position:absolute;top:65px;left:0;width:403px;height:208px;background:var(--cream)}
.split__intro h1{position:absolute;left:81px;font-size:36px;font-weight:500;line-height:44px}
.split__body{position:absolute;left:78px;top:300px;width:275px;font-family:"Barlow Condensed",sans-serif;font-weight:300;font-size:17px;line-height:22px}
.split__photo{position:absolute;left:406px;top:65px;width:424px;height:495px}

/* gallery */
.gallery-band{position:absolute;top:60px;left:0;width:830px;height:173px;background:var(--cream);display:flex;align-items:center;justify-content:center}
.gallery-band h1{font-size:36px;font-weight:500;padding-top:50px}
.gallery-group{position:absolute;left:94px;width:650px}
.gallery-group h2{display:flex;align-items:center;gap:16px;font-family:"Barlow Condensed",sans-serif;font-weight:400;font-size:17px}
.gallery-group h2::after{content:"";flex:1;height:1px;background:var(--rule)}
.thumbs{display:flex;gap:16px;margin-top:16px}
.thumbs figure{width:152px}
.thumbs .photo{width:152px;height:98px}
.thumbs figcaption{margin-top:10px;font-family:"Barlow Condensed",sans-serif;font-size:11px}
</style>
</head>
<body>

<!-- Home -->
<section class="page page--home">
  <header class="site-header">
    <div class="brand"><span class="brand__mark"></span><span class="brand__name">Quenford<br>Pier Hall</span></div>
    <nav class="main-nav"><span class="has-menu">About the building</span><span>Calendar</span><span>Public Exhibitions</span><span>Tour the building</span><span>Plan your visit</span><span>Contact us</span></nav>
  </header>
  <div class="hero photo" role="img" aria-label="Ornate gilded ferry terminal facade under a bright blue sky"></div>
  <div class="welcome">
    <h1>Welcome to the<br>Quenford Pier Hall</h1>
    <p>The majestic Quenford Pier Hall is located at the southern tip of Manhattan. Built in 1909, the building is the last remaining historic working ferry terminal in New York City.</p>
  </div>
  <article class="feature feature--hours">
    <h2>Hours</h2>
    <div class="photo" role="img" aria-label="Terminal building seen from the street on a sunny day" style="background:linear-gradient(180deg,#6d98c9 0%,#c9d6e2 40%,#8a7a4a 65%,#5b5b58 100%)"></div>
    <p>Check the calendar to see our hours of operation.</p>
    <span class="btn">Go to calendar <svg viewBox="0 0 14 8"><path d="M0 4h12M9 1l3 3-3 3" fill="none" stroke="currentColor" stroke-width="1.2"/></svg></span>
  </article>
  <article class="feature feature--history">
    <h2>History</h2>
    <div class="photo" role="img" aria-label="Black and white photo of the terminal entrance at night" style="background:linear-gradient(180deg,#4a4a4a,#1e1e1e)"></div>
    <p>A building of New York City's maritime history</p>
    <span class="btn">Our mission <svg viewBox="0 0 14 8"><path d="M0 4h12M9 1l3 3-3 3" fill="none" stroke="currentColor" stroke-width="1.2"/></svg></span>
  </article>

  <h2 class="events-title" style="font-weight:400">What to see</h2>
  <div class="event" style="top:1105px">
    <div class="photo" role="img" aria-label="Colourful painted artwork from the exhibition" style="background:linear-gradient(135deg,#d9563a,#3b8fb8 50%,#e7c13c)"></div>
    <span class="event__day">09</span><span class="event__meta">Sat<br>Jan</span>
    <span class="event__title">Exhibition tour event</span><span class="btn">Register</span>
  </div>
  <div class="event" style="top:1240px">
    <div class="photo" role="img" aria-label="Terminal facade on the waterfront" style="background:linear-gradient(180deg,#9bb6d1,#5d6b70 60%,#2f3a40)"></div>
    <span class="event__day">12</span><span class="event__meta">Sat<br>Jan</span>
    <span class="event__title">Exhibition tour event</span><span class="btn">Register</span>
  </div>
  <div class="event" style="top:1375px;border-bottom:none">
    <div class="photo" role="img" aria-label="Terminal building at street level" style="background:linear-gradient(180deg,#a9c0d6,#7a6c45 55%,#6a6a66)"></div>
    <span class="event__day">25</span><span class="event__meta">Sat<br>Jan</span>
    <span class="event__title">Exhibition tour event</span><span class="btn">Register</span>
  </div>

  <footer class="site-footer">
    <nav><span>About the building</span><span>Calendar</span><span>Public Exhibitions</span><span>Tour the building</span><span>Plan your visit</span><span>Contact us</span></nav>
    <div class="social"><i></i><i></i><i></i></div>
  </footer>
</section>

<!-- Mission -->
<section class="page page--mission">
  <header class="site-header">
    <div class="brand"><span class="brand__mark"></span><span class="brand__name">Quenford<br>Pier Hall</span></div>
    <nav class="main-nav"><span class="has-menu">About the building</span><span>Calendar</span><span>Public Exhibitions</span><span>Tour the building</span><span>Plan your visit</span><span>Contact us</span></nav>
  </header>
  <div class="split__intro"><h1 style="top:80px">Our Mission</h1></div>
  <p class="split__body">Lorem ipsum dolor sit amet, consectetur adipiscing elit. Eget accumsan platea sapien, mattis fusce egestas amet. Sit tincidunt ultrices massa imperdiet. Hendrerit in enim, eros amet tristique dui. Tortor, aenean egestas sed accumsan at proin. Viverra tellus massa convallis purus quam sit nulla amet. Fringilla proin magna facilisi sed. Diam vivamus ut gravida hendrerit ultrices ultricies non elementum. Vestibulum et id.</p>
  <div class="split__photo photo" role="img" aria-label="Black and white close-up of ornamental iron gate detail with an anchor motif" style="background:linear-gradient(90deg,var(--mono-dark),#8d8d8d 50%,var(--mono-dark))"></div>
  <footer class="site-footer">
    <nav><span>About the building</span><span>Calendar</span><span>Public Exhibitions</span><span>Tour the building</span><span>Plan your visit</span><span>Contact us</span></nav>
    <div class="social"><i></i><i></i><i></i></div>
  </footer>
</section>

<!-- Gallery -->
<section class="page page--gallery">
  <header class="site-header">
    <div class="brand"><span class="brand__mark"></span><span class="brand__name">Quenford<br>Pier Hall</span></div>
    <nav class="main-nav"><span class="has-menu">About the building</span><span>Calendar</span><span>Public Exhibitions</span><span>Tour the building</span><span>Plan your visit</span><span>Contact us</span></nav>
  </header>
  <div class="gallery-band"><h1>Gallery</h1></div>
  <div class="gallery-group" style="top:262px">
    <h2>History Photo</h2>
    <div class="thumbs">
      <figure><div class="photo" role="img" aria-label="Archival photo of the terminal from the water" style="background:linear-gradient(180deg,#c9c9c9,#555)"></div><figcaption>Harbor Builders Journal, 1909</figcaption></figure>
      <figure><div class="photo" role="img" aria-label="South facade with city towers behind" style="background:linear-gradient(180deg,#9db8d0,#6b7a6a 60%,#3d4a52)"></div><figcaption>South Facade</figcaption></figure>
      <figure><div class="photo" role="img" aria-label="East facade corner tower" style="background:linear-gradient(180deg,#5d8cc4,#b1a27a 60%,#4a4a48)"></div><figcaption>East Facade</figcaption></figure>
      <figure><div class="photo" role="img" aria-label="Archival street view of the terminal" style="background:linear-gradient(180deg,#d3d3d3,#6a6a6a)"></div><figcaption>Harbor Builders Journal, 1909</figcaption></figure>
    </div>
  </div>
  <div class="gallery-group" style="top:467px">
    <h2>Current Photo</h2>
    <div class="thumbs">
      <figure><div class="photo" role="img" aria-label="Gilded facade under blue sky" style="background:linear-gradient(160deg,#3e78c2,#8e7a3e 60%,#3e3420)"></div><figcaption>Harbor Builders Journal, 1909</figcaption></figure>
      <figure><div class="photo" role="img" aria-label="Green and gold ornamental doorways" style="background:linear-gradient(90deg,#5a3d2a,#b99a5a 50%,#5a3d2a)"></div><figcaption>South Facade</figcaption></figure>
      <figure><div class="photo" role="img" aria-label="Grand interior staircase" style="background:linear-gradient(180deg,#2a2a30,#6b6b72 60%,#1d1d20)"></div><figcaption>East Facade</figcaption></figure>
      <figure><div class="photo" role="img" aria-label="Restored great hall with skylight" style="background:linear-gradient(180deg,#cfd7de,#b8a57a 60%,#6f6450)"></div><figcaption>Harbor Builders Journal, 1909</figcaption></figure>
    </div>
  </div>
  <footer class="site-footer">
    <nav><span>About the building</span><span>Calendar</span><span>Public Exhibitions</span><span>Tour the building</span><span>Plan your visit</span><span>Contact us</span></nav>
    <div class="social"><i></i><i></i><i></i></div>
  </footer>
</section>

<!-- Building history -->
<section class="page page--history">
  <header class="site-header">
    <div class="brand"><span class="brand__mark"></span><span class="brand__name">Quenford<br>Pier Hall</span></div>
    <nav class="main-nav"><span class="has-menu">About the building</span><span>Calendar</span><span>Public Exhibitions</span><span>Tour the building</span><span>Plan your visit</span><span>Contact us</span></nav>
  </header>
  <div class="split__intro"><h1 style="top:60px">Building<br>History</h1></div>
  <p class="split__body">Lorem ipsum dolor sit amet, consectetur adipiscing elit. Eget accumsan platea sapien, mattis fusce egestas amet. Sit tincidunt ultrices massa imperdiet. Hendrerit in enim, eros amet tristique dui. Tortor, aenean egestas sed accumsan at proin. Viverra tellus massa convallis purus quam sit nulla amet. Fringilla proin magna facilisi sed. Diam vivamus ut gravida hendrerit ultrices ultricies non elementum. Vestibulum et id.</p>
  <div class="split__photo photo" role="img" aria-label="Archival black and white photo of the great hall interior with skylight and columns" style="background:linear-gradient(180deg,#6a6a6a,#c4c4c4 45%,var(--stone) 100%)"></div>
  <footer class="site-footer">
    <nav><span>About the building</span><span>Calendar</span><span>Public Exhibitions</span><span>Tour the building</span><span>Plan your visit</span><span>Contact us</span></nav>
    <div class="social"><i></i><i></i><i></i></div>
  </footer>
</section>

</body>
</html>
```